Company Services Brochure - Harborlight Advisory Partners

I need a brochure detailing our company and making a solid value proposition for what we do and our services. I need it by Tuesday for a big meeting Thursday. The website is www.harborlightadvpart.com

The company focuses on partnering with our clients to accomplish big goals and solve challenges through people and strategy. We are certified executive coaches and leadership developers (we train and coach leaders), and we develop and monitor strategic plans and the implementation of the plan. Managing Partner - R. Milton Crowe and Senior Parter - Dana Pritchett .... pics are attached....please let me know whatever else you need and I can upload.
Updates

This would be a trifold - front back for our potential clients.... We work in all industries - public, private, government, education, nonprofit, faith based, etc. Please let me know if you have other questions. And, please be creative!!

```html
<!DOCTYPE html>
<html lang="en">
<head>
<meta charset="utf-8">
<title>Harborlight Advisory Partners – Trifold Brochure</title>
<link href="https://fonts.googleapis.com/css2?family=Montserrat:wght@500;600;800&family=Roboto:wght@400;500;700&family=Roboto+Condensed:wght@700&display=swap" rel="stylesheet">
<style>
:root{
  --navy:#2c3a55;
  --navy-deep:#24304a;
  --blue:#1f6fcb;
  --grey:#6e7074;
  --pill:#77787b;
  --paper:#ffffff;
  --paper-shade:#eeeeef;
  --ink:#222;
  --stage:#6a6e75;
}
*{margin:0;padding:0;box-sizing:border-box}
html,body{width:1200px;height:2446px;overflow:hidden}
body{background:linear-gradient(180deg,#5b5f66,#7b7f86 55%,#5f636a);font-family:"Roboto",sans-serif;color:var(--ink);position:relative}
.brochure{position:absolute;left:30px;top:778px;width:1140px;height:890px;background:var(--paper);box-shadow:0 10px 30px rgba(0,0,0,.35);display:flex}
.panel{position:relative;height:100%}
.panel-left{width:380px}
.panel-middle{width:375px;background:linear-gradient(90deg,var(--paper-shade),var(--paper) 12%,var(--paper) 88%,var(--paper-shade))}
.panel-right{width:385px}
.band-top{position:absolute;left:0;right:0;top:0;height:208px;display:flex;flex-direction:column;align-items:center;justify-content:center;text-align:center}
.band-dark{position:absolute;left:0;right:0;top:208px;height:417px;background:var(--navy);color:#fff}
.band-stripe{position:absolute;left:0;right:0;top:625px;height:15px;background:var(--blue)}
.band-bottom{position:absolute;left:0;right:0;top:640px;height:250px}
.wordmark{font-family:"Montserrat",sans-serif;font-weight:600;color:var(--blue);font-size:30px;line-height:1.15;letter-spacing:.2px}
.section-title{font-family:"Montserrat",sans-serif;font-weight:500;font-size:25px;text-align:center;letter-spacing:.3px}
.about{padding:22px 28px 0}
.about p{font-size:12.3px;line-height:15.6px;text-align:justify;margin-top:12px;font-weight:400}
.about .lead{margin-top:18px;text-align:left}
.about .lead strong{font-weight:700;display:block}
.mission{margin-top:18px}
.mission p{text-align:center;margin-top:10px;padding:0 10px}
.photo{position:absolute;inset:0}
.photo-meeting{background:linear-gradient(135deg,#c9ccd1,#8d97a6 45%,#4d5566)}
.photo-students{background:linear-gradient(160deg,#3b4556,#232a37 55%,#4a3a30)}
.quote{padding:0 32px;font-size:11.3px;line-height:15.4px;color:#333}
.quote-source{margin-top:14px;font-weight:700;color:var(--blue);font-size:20px}
.team{padding-top:22px}
.member{position:absolute;left:18px;width:338px;height:132px}
.member .card{position:absolute;left:72px;top:6px;width:262px;height:126px;border:1px solid #8d96a8;border-radius:6px}
.member .portrait{position:absolute;left:0;top:0;width:136px;height:136px;border-radius:50%;border:6px solid #b9bcc2;background:radial-gradient(circle at 50% 40%,#8a6b5a,#3b2c26 70%)}
.member .info{position:absolute;left:150px;top:28px}
.member .name{font-family:"Roboto Condensed",sans-serif;font-weight:700;color:var(--blue);font-size:20px;letter-spacing:-.2px}
.member .role{font-size:11.5px;font-weight:700;margin-top:6px}
.member .email{font-size:11px;margin-top:4px}
.social{display:flex;gap:5px;margin-top:8px}
.social span{width:16px;height:16px;border-radius:50%;background:#9ea4ae}
.contact{text-align:center;padding-top:42px}
.contact .section-title{color:var(--blue)}
.contact-icons{display:flex;justify-content:center;gap:4px;margin:10px 0 8px}
.contact address{font-style:normal;font-size:14.5px;line-height:19.5px}
.url-pill{position:absolute;left:38px;top:195px;width:297px;height:56px;border-radius:10px 10px 0 0;background:var(--pill);color:#fff;font-size:15px;display:flex;align-items:center;justify-content:center;padding-bottom:8px}
.cover-copy{text-align:center;padding-top:32px}
.cover-title{font-family:"Montserrat",sans-serif;font-weight:800;color:var(--blue);font-size:44px;line-height:44px;letter-spacing:.5px}
.cover-sub{font-size:16px;line-height:20px;margin-top:12px}
.cover-url{color:var(--blue);font-size:15px;margin-top:22px}
</style>
</head>
<body>
<main class="brochure">

  <section class="panel panel-left">
    <div class="band-top">
      <div class="wordmark">Harborlight<br>Advisory Partners</div>
    </div>
    <div class="band-dark">
      <div class="about">
        <h2 class="section-title">ABOUT US</h2>
        <p>Harborlight Advisory Partners (HAP) is a boutique professional services consulting practice committed to assisting clients in all industries accomplish their biggest goals and solve their toughest challenges. Our partners are accomplished leaders who are experts in their disciplines and take extreme pride in their work. While our partners are experts in their chosen field, our firm believes the best approach to problem-solving is to use a cross-disciplinary team. Each engagement is specifically tailored to the needs of our diverse and unique clientele.</p>
        <p class="lead"><strong>What Makes HAP Stand Out?</strong>Our belief in relationships! We value you and your goals are our goals – Bottom Line!</p>
        <div class="mission">
          <h2 class="section-title">MISSION STATEMENT</h2>
          <p>To provide unmatched customer service to every client facilitating real results through a deliberate focus on people, strategy, leadership, and equity.</p>
        </div>
      </div>
    </div>
    <div class="band-stripe"></div>
    <div class="band-bottom">
      <div class="photo photo-meeting" role="img" aria-label="Photo of colleagues talking around a table in a bright office meeting"></div>
    </div>
  </section>

  <section class="panel panel-middle">
    <div class="band-top">
      <p class="quote">“Our experience with the Harborlight team was just different. From the beginning, we could tell it was about relationship for them, and teamwork mattered. This made it feel like we were in it together as they partnered with us and facilitated our improvement, which made it sustainable.”</p>
      <p class="quote-source">New Nonprofit CEO</p>
    </div>
    <div class="band-dark team">
      <h2 class="section-title">OUR TEAM</h2>
      <div class="member" style="top:68px">
        <div class="card"></div>
        <div class="portrait" role="img" aria-label="Portrait photo of Senior Partner Dana Pritchett"></div>
        <div class="info">
          <div class="name">DR. DANA PRITCHETT</div>
          <div class="role">Senior Partner</div>
          <div class="email">dpritchett@harborlightadvpart.com</div>
          <div class="social"><span></span><span></span><span></span></div>
        </div>
      </div>
      <div class="member" style="top:220px">
        <div class="card"></div>
        <div class="portrait" role="img" aria-label="Portrait photo of Managing Partner R. Milton Crowe"></div>
        <div class="info">
          <div class="name">R. MILTON CROWE, PH.D.</div>
          <div class="role">Managing Partner</div>
          <div class="email">rmc@harborlightadvpart.com</div>
          <div class="social"><span></span><span></span><span></span></div>
        </div>
      </div>
    </div>
    <div class="band-stripe"></div>
    <div class="band-bottom contact">
      <h2 class="section-title">CONTACT US</h2>
      <div class="contact-icons">
        <svg width="16" height="16" viewBox="0 0 16 16"><circle cx="8" cy="8" r="8" fill="var(--blue)"/><path d="M8 3.5a3 3 0 0 0-3 3c0 2.2 3 5.5 3 5.5s3-3.3 3-5.5a3 3 0 0 0-3-3z" fill="#fff"/><circle cx="8" cy="6.5" r="1.1" fill="var(--blue)"/></svg>
        <svg width="16" height="16" viewBox="0 0 16 16"><circle cx="8" cy="8" r="8" fill="var(--blue)"/><path d="M5 4.5l1.6-.3.9 2-1 .8a5.5 5.5 0 0 0 2.5 2.5l.8-1 2 .9-.3 1.6c-3.7.2-6.7-2.8-6.5-6.5z" fill="#fff"/></svg>
        <svg width="16" height="16" viewBox="0 0 16 16"><circle cx="8" cy="8" r="8" fill="var(--blue)"/><rect x="4" y="5" width="8" height="6" rx="1" fill="#fff"/><path d="M4.3 5.5L8 8.3l3.7-2.8" stroke="var(--blue)" stroke-width="1" fill="none"/></svg>
      </div>
      <address>4410 Larkspur Parkway, Suite 310<br>Ashford, Virginia 23190<br>(555) 214-7730<br>info@harborlightadvpart.com</address>
      <div class="url-pill">www.harborlightadvpart.com</div>
    </div>
  </section>

  <section class="panel panel-right">
    <div class="band-top">
      <div class="wordmark">Harborlight<br>Advisory Partners</div>
    </div>
    <div class="band-dark" style="height:432px">
      <div class="photo photo-students" role="img" aria-label="Photo of smiling young people gathered together, in dark blue tones"></div>
    </div>
    <div class="band-bottom cover-copy">
      <h1 class="cover-title">PROVIDING<br>SOLUTIONS</h1>
      <p class="cover-sub">Helping clients accomplish their biggest<br>goals and solve their toughest challenges<br>in ALL industries.</p>
      <p class="cover-url">www.harborlightadvpart.com</p>
    </div>
  </section>

</main>
</body>
</html>
```